SEO Agentur www.tornblau.de - Webseite soll neu designed werden (Start- und Unterseite)
Zielgruppe
Alle Infos sind auf der Seite www.tornblau.de enthalten.
Aufgabenstellung
Die Seite soll neu gestalltet werden. Wir möchten gerne ein wenig professioneller werden. Der Name der Seite zwingt uns allerdings ein gewisses Thema auf.
Die Aufgabe:
Ein professionelleres Design der Startseite und einer Unterseite. Die Programmierung machen wir selbst. Thema Suche und Helden muss bleiben aufgrund der URL.
Mit dem Gewinner würden wir dann auch geren jedes Element der Seite durchgehen und neu gestallten (separater Auftrag).
Das Novaflux Logo ist aufgrund des neuen Films auch gewaltiger und seriöser geworden. Vielleicht kann man daran anknüpfen. Ist aber keine Bedingung nur eine kleine Idee.
Wir werden alle Vorschläge ca. 50 Leuten vorstellen und dann den Vorschlag mit den meisten Stimmen wählen.

```html
<!DOCTYPE html>
<html lang="de">
<head>
<meta charset="utf-8">
<title>Tornblau – Wir finden Helden!</title>
<link rel="stylesheet" href="https://fonts.googleapis.com/css2?family=Bebas+Neue&family=Source+Sans+3:wght@400;600;700&display=swap">
<style>
  :root {
    --dark: #3d3d3d;
    --footer: #383838;
    --blue: #0a9ee0;
    --text: #3a3a3a;
    --white: #ffffff;
    --badge: #f5d90a;
  }
  * { margin: 0; padding: 0; box-sizing: border-box; }
  html, body { width: 764px; height: 1200px; overflow: hidden; background: var(--white); }
  body { position: relative; font-family: "Source Sans 3", sans-serif; color: var(--text); }

  .site-header { position: absolute; left: 0; top: 0; width: 764px; height: 72px; background: var(--dark); border-bottom: 3px solid var(--blue); z-index: 2; }
  .main-nav { position: absolute; left: 41px; top: 32px; display: flex; }
  .main-nav a { display: block; height: 37px; line-height: 33px; color: var(--white); text-decoration: none; font-size: 11.5px; }
  .main-nav a.is-active { background: var(--blue); padding: 0 10px; }
  .nav-ablauf { margin-left: 36px; }
  .nav-vorteile { margin-left: 44px; }
  .nav-leistungen { margin-left: 47px; }
  .nav-infos { margin-left: 41px; }
  .nav-blog { margin-left: 43px; }

  .brand { position: absolute; left: 600px; top: 30px; display: flex; align-items: center; gap: 7px; color: var(--white); font-size: 19px; font-weight: 700; }
  .brand-dot { width: 12px; height: 12px; border-radius: 50%; background: var(--badge); }

  .hero { position: absolute; left: 0; top: 72px; width: 764px; height: 263px;
    background: linear-gradient(180deg, #d6d6d6 0%, #a9a9a9 30%, #6a6a6a 60%, #2e2e2e 100%); }
  .hero-title { position: absolute; left: 286px; top: 140px; font-family: "Bebas Neue", sans-serif; font-size: 66px; line-height: 1; color: var(--white); letter-spacing: 0.5px; }
  .hero-sub { position: absolute; left: 287px; top: 203px; font-size: 18px; color: var(--white); }

  .feature-badge { position: absolute; top: 366px; width: 120px; height: 97px; }
  .feature-label { position: absolute; color: var(--blue); font-size: 13.5px; line-height: 1; white-space: nowrap; }
  .feature-label strong { font-weight: 700; }

  .feature-text { position: absolute; top: 506px; width: 194px; font-size: 14.8px; line-height: 17.9px; letter-spacing: 0.15px; }
  .feature-text p + p { margin-top: 12px; }

  .site-footer { position: absolute; left: 0; top: 1072px; width: 764px; height: 128px; background: var(--footer); border-top: 3px solid var(--blue); box-shadow: 0 -3px 4px rgba(0,0,0,0.25); color: var(--white); font-size: 9px; line-height: 12px; }
  .footer-col { position: absolute; top: 13px; }
  .footer-col p + p { margin-top: 3px; }
  .footer-divider { position: absolute; left: 174px; top: 14px; width: 1px; height: 108px; background: #666; }
  .footer-legal { position: absolute; left: 618px; top: 100px; font-size: 11.5px; color: var(--blue); }
</style>
</head>
<body>
  <header class="site-header">
    <nav class="main-nav">
      <a class="is-active" href="#">Startseite</a>
      <a class="nav-ablauf" href="#">Ablauf</a>
      <a class="nav-vorteile" href="#">Ihre Vorteile</a>
      <a class="nav-leistungen" href="#">Unsere Leistungen</a>
      <a class="nav-infos" href="#">Infos</a>
      <a class="nav-blog" href="#">Blog</a>
    </nav>
    <div class="brand"><span class="brand-dot"></span>Tornblau</div>
  </header>

  <section class="hero" role="img" aria-label="Schwarz-weißes Foto einer Großstadt-Skyline">
    <h1 class="hero-title">WIR FINDEN HELDEN!</h1>
    <p class="hero-sub">Suchmaschinenoptimierung für Ihre Website</p>
  </section>

  <svg class="feature-badge" style="left:7px" viewBox="0 0 120 97" aria-hidden="true">
    <polygon points="23,0 97,0 120,24 60,97 0,24" fill="var(--dark)"/>
    <g fill="none" stroke="#fff" stroke-width="2.2" stroke-linejoin="round">
      <rect x="36" y="30" width="8" height="22" fill="#fff"/>
      <path d="M47 52 V32 L54 22 V10 Q60 8 61 16 L59 27 H75 Q79 28 77 33 Q80 36 76 39 Q79 42 75 45 Q77 49 72 52 Z"/>
    </g>
  </svg>
  <div class="feature-label" style="left:116px;top:407px"><strong>Grantiert</strong> zufrieden!</div>
  <div class="feature-label" style="left:101px;top:429px">falls nicht</div>
  <div class="feature-label" style="left:79px;top:452px">100% Geld zurück</div>

  <svg class="feature-badge" style="left:275px" viewBox="0 0 120 97" aria-hidden="true">
    <polygon points="23,0 97,0 120,24 60,97 0,24" fill="var(--dark)"/>
    <circle cx="54" cy="30" r="11" fill="none" stroke="#fff" stroke-width="5"/>
    <line x1="62" y1="38" x2="75" y2="51" stroke="#fff" stroke-width="7" stroke-linecap="round"/>
  </svg>
  <div class="feature-label" style="left:389px;top:407px"><strong>SEO</strong></div>
  <div class="feature-label" style="left:377px;top:429px">Suchmaschinen -</div>
  <div class="feature-label" style="left:359px;top:452px">Optimierung</div>

  <svg class="feature-badge" style="left:528px" viewBox="0 0 120 97" aria-hidden="true">
    <polygon points="23,0 97,0 120,24 60,97 0,24" fill="var(--dark)"/>
    <polyline points="40,40 52,52 72,28" fill="none" stroke="#fff" stroke-width="3"/>
    <polyline points="62,28 72,28 72,38" fill="none" stroke="#fff" stroke-width="3"/>
  </svg>
  <div class="feature-label" style="left:644px;top:407px"><strong>SEO</strong></div>
  <div class="feature-label" style="left:630px;top:429px">Suchmaschinen -</div>
  <div class="feature-label" style="left:614px;top:452px">Optimierung</div>

  <div class="feature-text" style="left:32px">
    <p>Lorem ipsum dolor sit amet, consetetur sadipscing elitr, sed diam nonumy eirmod tempor invidunt ut labore et dolore magna aliquyam erat, sed diam voluptua. At vero eos et accusam et justo duo dolores et ea rebum. Stet clita kasd gubergren, no sea takimata sanctus est Lorem ipsum dolor sit amet.</p>
    <p>Lorem ipsum dolor sit amet, consetetur sadipscing elitr, sed diam nonumy eirmod tempor</p>
  </div>
  <div class="feature-text" style="left:280px">
    <p>Lorem ipsum dolor sit amet, consetetur sadipscing elitr, sed diam nonumy eirmod tempor invidunt ut labore et dolore magna aliquyam erat, sed diam voluptua. At vero eos et accusam et justo duo dolores et ea rebum. Stet clita kasd gubergren, no sea takimata sanctus est Lorem ipsum dolor sit amet.</p>
    <p>Lorem ipsum dolor sit amet, consetetur sadipscing elitr, sed diam nonumy eirmod tempor</p>
  </div>
  <div class="feature-text" style="left:538px">
    <p>Lorem ipsum dolor sit amet, consetetur sadipscing elitr, sed diam nonumy eirmod tempor invidunt ut labore et dolore magna aliquyam erat, sed diam voluptua. At vero eos et accusam et justo duo dolores et ea rebum. Stet clita kasd gubergren, no sea takimata sanctus est Lorem ipsum dolor sit amet.</p>
    <p>Lorem ipsum dolor sit amet, consetetur sadipscing elitr, sed diam nonumy eirmod tempor</p>
  </div>

  <footer class="site-footer">
    <div class="footer-col" style="left:41px">
      <p>Tornblau.de GbR<br>Lindenweg 14<br>29451 Harzmoor</p>
      <p>Impressum<br>Zum Kontaktformular</p>
      <p>Hotline 0555 - 310 482 90<br>Wir warten auf Ihren Anruf</p>
    </div>
    <div class="footer-divider"></div>
    <div class="footer-col" style="left:196px">
      <p>Suchmaschinenoptimierung</p>
      <p>SEO Agentur<br>SEO Marketing<br>SEO Umsatz<br>Suchmaschinenoptimierung Agentur<br>SEO Agentur Erfolgsbasiert</p>
    </div>
    <div class="footer-col" style="left:387px">
      <p>Suchmaschinenwerbung</p>
      <p>Klickwerk Agentur<br>Klickwerk Anzeigen<br>SEA Agentur<br>SEM Agentur</p>
    </div>
    <div class="footer-col" style="left:525px">
      <p>Erklärvideos</p>
      <p>Webseiten<br>Erklärfilme<br>Produktvideos</p>
    </div>
    <div class="footer-legal">Impressum | Kontakt</div>
  </footer>
</body>
</html>
```